Create a dynamisch, inspiring PowerPoint Design master for our company Brightway & Partners

Core business: Coaching, Consulting and Executive search

The PPT master should be easy to use and include professional formatting (using the fonts of our website). In general, the slide master should have the look and feel of our website (in terms of fonts, colors, logos) We also would like to place big photographs on some slides, having text and graph slides as well as photo slides with just 1 key message or a citation.

The PowerPoint design should fit our corporate Identity www.brightway-partners.de
I have enclosed the PPT we use now.

Logos und colors are attached, also the master PPD we now use. We need the new master to be more modern, dynamisch und nicht so dreary, grey, but far more attractive and inspiring. If necessary we ca add a new color to make it more attractive. Please advise.

Additional information:
- wide screen format - 16:9
- creation of chart templates, using chart tools, and different chart types etc.
- creation of different slide layouts to place content, pictures (in different sizes), optionally Media
- as well as standard elements, such as text boxes, lines, default shapes, etc.

We have received your contact info and recommondations from Renate Kolbeck-Strauss. We liked the master you designed very much and would like that kind of style. I can send you her presentation as a reminder if needed?

```html
<!DOCTYPE html>
<html lang="en">
<head>
<meta charset="utf-8">
<title>Brightway &amp; Partners – Presentation Master</title>
<link rel="stylesheet" href="https://fonts.googleapis.com/css2?family=Roboto:wght@300;400;500;700;900&display=swap">
<style>
:root{
  --board:#2a2a2a;
  --teal:#1c6f68;
  --teal-dark:#0f4a45;
  --teal-bright:#2ec4b6;
  --chart-a:#3bb8c4;
  --chart-b:#5fc7d8;
  --navy:#1d2340;
  --ink:#333;
  --grey:#6a6a6a;
  --white:#fff;
}
*{box-sizing:border-box;margin:0;padding:0}
html,body{width:1200px;height:4835px;overflow:hidden}
body{background:var(--board);font-family:'Roboto',sans-serif;color:var(--ink);position:relative}
.slide{position:absolute;left:45px;width:1110px;background:var(--white);overflow:hidden}
.abs{position:absolute}

/* title slide */
.slide--title{top:71px;height:737px}
.title-photo{position:absolute;inset:0;background:linear-gradient(135deg,#6f7f7e 0%,#9aa3a2 40%,#b9bebd 70%,#cfd2d1 100%)}
.title-shapes{position:absolute;inset:0}
.brand{position:absolute;text-align:right}
.brand__name{font-family:'Roboto',sans-serif;font-weight:300;color:#3d3d3d;font-size:46px;letter-spacing:.5px;line-height:1}
.brand__tag{font-size:11.5px;letter-spacing:.6px;color:#3d3d3d;margin-top:6px}

/* intro slide */
.slide--intro{top:851px;height:747px}
.heading{color:var(--teal);font-weight:700;font-size:34px;line-height:1.35;text-transform:uppercase}
.subheading{color:var(--navy);font-weight:700;font-size:20px;line-height:1.6;text-transform:uppercase}
.body{font-size:15.5px;line-height:1.5;color:var(--ink)}
.body--justify{text-align:justify}
.intro-list p{font-size:15.5px;line-height:2}
.intro-image{position:absolute;left:745px;top:98px;width:200px;height:592px;border-radius:100px;background:linear-gradient(180deg,#7fa9c3 0%,#c8d6de 35%,#b7795f 65%,#253344 100%)}

/* services slide */
.slide--services{top:1645px;height:746px}
.service-rings{position:absolute;left:0;top:0}
.service{position:absolute;width:320px;text-align:center}
.service__title{font-weight:700;font-size:15.5px;line-height:1.65;color:var(--navy);text-transform:uppercase}
.service__rule{width:58px;height:2px;background:var(--navy);margin:14px auto 18px}
.service__text{font-size:13.5px;line-height:1.6;color:#444}

/* chart slide */
.slide--chart{top:2436px;height:783px}
.chart-photo{position:absolute;left:39px;top:49px;width:1032px;height:362px;background:linear-gradient(90deg,#d9d6d2 0%,#3c5f8f 35%,#2b4d86 55%,#5b6470 80%,#e9e9e9 100%)}
.chart-card{position:absolute;left:72px;top:219px;width:965px;height:538px;background:var(--white)}
.chart-card__title{position:absolute;top:30px;width:100%;text-align:center;font-weight:500;font-size:25px;color:#111}

/* coaching slide */
.slide--coaching{top:3272px;height:676px}
.coaching-image{position:absolute;left:105px;top:124px;width:440px;height:440px;border-radius:50%;background:radial-gradient(circle at 40% 40%,#1f7a72 0%,var(--teal) 55%,var(--teal-dark) 100%)}
.coaching-copy{position:absolute;left:632px;top:136px;width:388px}
.coaching-copy .subheading{font-size:16.5px;line-height:1.6;margin-top:22px}
.coaching-copy .body{font-size:16px;margin-top:20px}

/* closing slide */
.slide--closing{top:4002px;height:740px;background:linear-gradient(180deg,#1a6e69 0%,#175f5c 45%,#0f4a4b 100%)}
.closing-photo{position:absolute;inset:0;background:linear-gradient(180deg,rgba(0,0,0,0) 40%,rgba(8,40,44,.55) 100%)}
.closing-brand{position:absolute;top:312px;width:100%;text-align:center;color:var(--white)}
.closing-brand .brand__name{color:var(--white);font-size:44px}
.closing-brand .brand__tag{color:var(--white)}
.closing-text{position:absolute;top:432px;left:190px;width:730px;text-align:center;color:var(--white);font-size:17px;line-height:1.55}
</style>
</head>
<body>

<!-- Title slide -->
<section class="slide slide--title">
  <div class="title-photo" role="img" aria-label="Photo from above of a team working around a round table with teal chairs"></div>
  <svg class="title-shapes" width="1110" height="737" viewBox="0 0 1110 737">
    <polygon points="668,0 1110,0 1110,398" fill="var(--teal-bright)"/>
    <polygon points="1110,430 1110,737 600,737" fill="#e4e5e5"/>
  </svg>
  <div class="brand" style="right:20px;top:622px">
    <div class="brand__name">brightway &amp; partners</div>
    <div class="brand__tag">TALENTE FINDEN, BEGLEITEN UND FÖRDERN</div>
  </div>
</section>

<!-- Intro slide -->
<section class="slide slide--intro">
  <div class="abs" style="left:70px;top:130px;width:560px">
    <h1 class="heading">Find, guide and<br>grow talents.</h1>
    <h2 class="subheading" style="margin-top:16px;font-size:19.5px">Your coaching &amp; executive search<br>experts from Brightway &amp; Partners</h2>
    <p class="body body--justify" style="margin-top:14px;width:485px">"Brightway &amp; Partners" is an amalgamation of the former Wendler-Coaching and the personnel consultancy of Tobias Wendler. We have expertise in the areas of executive search, management diagnostics and leadership development. We take care of your executives - with great professional depth and with the many years of experience of an exceptionally broad-based team. As such ...</p>
    <div class="intro-list" style="margin-top:16px">
      <p>... we will find the right candidates for you</p>
      <p>... we evaluate your existing management team</p>
      <p>... we raise and develop existing competencies in your company.</p>
      <p>... we work on your topics and potential as a single person</p>
    </div>
  </div>
  <div class="intro-image" role="img" aria-label="City skyline and world map photograph in a tall rounded frame"></div>
</section>

<!-- Services slide -->
<section class="slide slide--services">
  <svg class="service-rings" width="1110" height="420" viewBox="0 0 1110 420">
    <defs>
      <linearGradient id="ringFill" x1="0" y1="0" x2="0" y2="1">
        <stop offset="0" stop-color="var(--teal)"/>
        <stop offset="1" stop-color="var(--teal-dark)"/>
      </linearGradient>
    </defs>
    <g fill="url(#ringFill)">
      <circle cx="208" cy="242" r="131"/>
      <circle cx="552" cy="242" r="131"/>
      <circle cx="888" cy="242" r="131"/>
    </g>
    <circle cx="208" cy="242" r="100" fill="var(--white)"/>
    <circle cx="552" cy="242" r="100" fill="#fbf8ee"/>
    <circle cx="888" cy="242" r="100" fill="var(--white)"/>
    <g fill="none" stroke="#222" stroke-width="3" stroke-linecap="round">
      <rect x="168" y="206" width="56" height="44" rx="4"/>
      <circle cx="212" cy="250" r="20" fill="var(--white)"/>
      <line x1="226" y1="264" x2="250" y2="288"/>
      <circle cx="520" cy="214" r="9"/><circle cx="552" cy="214" r="9"/><circle cx="584" cy="214" r="9"/>
      <path d="M508 250 v-18 h24 v18 M540 250 v-18 h24 v18 M572 250 v-18 h24 v18"/>
      <line x1="500" y1="252" x2="604" y2="252"/>
      <line x1="512" y1="252" x2="512" y2="282"/><line x1="592" y1="252" x2="592" y2="282"/>
      <rect x="858" y="204" width="60" height="28"/>
      <line x1="888" y1="232" x2="888" y2="246"/>
      <rect x="852" y="246" width="72" height="24"/>
      <line x1="862" y1="270" x2="862" y2="284"/><line x1="914" y1="270" x2="914" y2="284"/>
    </g>
  </svg>
  <div class="service" style="left:48px;top:424px">
    <div class="service__title">Executive search</div>
    <div class="service__rule"></div>
    <p class="service__text">Brightway &amp; Partners pursues a leadership development approach that goes beyond the mere placement business of classic headhunters. Our strategic personnel consulting is individually tailored to the current needs and the long-term development prospects of companies</p>
  </div>
  <div class="service" style="left:392px;top:424px">
    <div class="service__title">Personnel development<br>and coaching</div>
    <div class="service__rule"></div>
    <p class="service__text">We provide holistic and interdisciplinary support both in personnel development, especially for executives, and in finding solutions to personal issues for individuals. We unite highly qualified business coaches with different focuses</p>
  </div>
  <div class="service" style="left:728px;top:424px">
    <div class="service__title">Management diagnostics</div>
    <div class="service__rule"></div>
    <p class="service__text">The personality, the performance and the potential of the executives of a company are an elementary prerequisite for its future viability. Therefore, the reliable analysis of the leadership qualities and development prospects of the existing management staff is a central</p>
  </div>
</section>

<!-- Chart slide -->
<section class="slide slide--chart">
  <div class="chart-photo" role="img" aria-label="Photo of a team discussing at a whiteboard"></div>
  <div class="chart-card">
    <div class="chart-card__title">Find, guide and grow talents</div>
    <svg class="abs" style="left:0;top:0" width="965" height="538" viewBox="0 0 965 538">
      <g stroke="#ececec" stroke-width="1">
        <line x1="82" y1="100" x2="905" y2="100"/><line x1="82" y1="138" x2="905" y2="138"/>
        <line x1="82" y1="176" x2="905" y2="176"/><line x1="82" y1="214" x2="905" y2="214"/>
        <line x1="82" y1="252" x2="905" y2="252"/><line x1="82" y1="290" x2="905" y2="290"/>
        <line x1="82" y1="328" x2="905" y2="328"/><line x1="82" y1="366" x2="905" y2="366"/>
        <line x1="82" y1="404" x2="905" y2="404"/><line x1="82" y1="442" x2="905" y2="442"/>
      </g>
      <g font-family="Roboto, sans-serif" font-size="10" fill="#555" text-anchor="end">
        <text x="58" y="104">45</text><text x="58" y="142">40</text><text x="58" y="180">35</text>
        <text x="58" y="218">30</text><text x="58" y="256">25</text><text x="58" y="294">20</text>
        <text x="58" y="332">15</text><text x="58" y="370">10</text><text x="58" y="408">5</text>
        <text x="58" y="446">0</text>
      </g>
      <g font-family="Roboto, sans-serif" font-size="9" fill="#555" text-anchor="middle">
        <text x="99" y="471">2000</text><text x="139" y="471">2001</text><text x="178" y="471">2002</text>
        <text x="218" y="471">2003</text><text x="258" y="471">2004</text><text x="298" y="471">2005</text>
        <text x="338" y="471">2006</text><text x="377" y="471">2007</text><text x="417" y="471">2008</text>
        <text x="457" y="471">2009</text><text x="497" y="471">2010</text><text x="537" y="471">2011</text>
        <text x="576" y="471">2012</text><text x="616" y="471">2013</text><text x="656" y="471">2014</text>
        <text x="696" y="471">2015</text><text x="736" y="471">2016</text><text x="775" y="471">2017</text>
        <text x="815" y="471">2018</text><text x="855" y="471">2019</text><text x="895" y="471">2020</text>
      </g>
      <path d="M99 336 C130 350,150 322,171 320 S215 366,242 366 S280 288,313 290 S360 298,384 298 S425 340,455 339 S500 318,526 320 S575 296,597 298 S640 324,668 324 S705 352,740 351 S790 290,812 290 S860 307,883 309"
            fill="none" stroke="var(--chart-b)" stroke-width="2"/>
      <path d="M99 396 C120 380,150 362,171 374 S215 276,242 275 S280 334,313 324 S360 314,384 320 S425 416,455 412 S500 380,526 381 S575 412,597 404 S640 290,668 290 S705 320,740 320 S790 410,812 412 S860 268,883 260"
            fill="none" stroke="var(--chart-a)" stroke-width="2"/>
      <g fill="var(--chart-b)">
        <circle cx="99" cy="336" r="4"/><circle cx="171" cy="320" r="4"/><circle cx="242" cy="366" r="4"/>
        <circle cx="313" cy="290" r="4"/><circle cx="384" cy="298" r="4"/><circle cx="455" cy="339" r="4"/>
        <circle cx="526" cy="320" r="4"/><circle cx="597" cy="298" r="4"/><circle cx="668" cy="324" r="4"/>
        <circle cx="740" cy="351" r="4"/><circle cx="812" cy="290" r="4"/><circle cx="883" cy="309" r="4"/>
      </g>
      <g fill="var(--chart-a)">
        <circle cx="99" cy="396" r="4"/><circle cx="171" cy="374" r="4"/><circle cx="242" cy="275" r="4"/>
        <circle cx="313" cy="324" r="4"/><circle cx="384" cy="320" r="4"/><circle cx="455" cy="412" r="4"/>
        <circle cx="526" cy="381" r="4"/><circle cx="597" cy="404" r="4"/><circle cx="668" cy="290" r="4"/>
        <circle cx="740" cy="320" r="4"/><circle cx="812" cy="412" r="4"/><circle cx="883" cy="260" r="4"/>
      </g>
    </svg>
  </div>
</section>

<!-- Coaching slide -->
<section class="slide slide--coaching">
  <div class="coaching-image" role="img" aria-label="Teal circular illustration with icons for company, consulting and team coaching"></div>
  <div class="coaching-copy">
    <h2 class="heading">Coaching for<br>everyone!</h2>
    <p class="subheading">Just take it easy! Why can't I just<br>say no? Don't be too big on yourself!<br>Just come on time! Why can't I<br>just relax?</p>
    <p class="body body--justify">Has any of these sentences really changed something - in yourself or in others?</p>
    <p class="body body--justify">Probably not. Because it is not easy to break up internalized thinking structures that have been in place for years and to discard well-practiced behavioral patterns. It doesn't just happen, and certainly not all by itself.</p>
  </div>
</section>

<!-- Closing slide -->
<section class="slide slide--closing">
  <div class="closing-photo" role="img" aria-label="Teal-toned city skyline photograph with a faint world map"></div>
  <div class="closing-brand">
    <div class="brand__name">brightway &amp; partners</div>
    <div class="brand__tag">TALENTE FINDEN, BEGLEITEN UND FÖRDERN</div>
  </div>
  <p class="closing-text">The success of our interdisciplinary projects proves that we are able to develop previously unused value potential for our customers through our new, comprehensive approach. With creativity, solidarity and, above all, real passion for working with people, we create special added value - both for companies and for individuals.</p>
</section>

</body>
</html>
```